New Wine Label - Argentinian Malbec 'Viento Callado'

I am looking for an exceptional and exciting design for a wine label called 'Viento Callado' meaning Quiet Wind or Wind of the Quiet. The design must feature the name 'Viento Callado', a star logo and the word 'Malbec'. It will also need the words 'Mendoza, Argentina' at the bottom of the label as a prominent piece of information. Please produce the work in size 80mm x 100mm. Feel free to use colour in addition to black/white and ensue that the label is easy to read on a shelf placement.

Target Market(s)

25-50 Year Olds who enjoy great wine that looks and appears interesting and a little different.

Requirements
Must have
• Star Logo
• Word - Malbec
• Words - Mendoza, Argentina
Nice to have
• Background image to label

```html
<!DOCTYPE html>
<html lang="en">
<head>
<meta charset="utf-8">
<title>Viento Callado Malbec Label</title>
<link rel="stylesheet" href="https://fonts.googleapis.com/css2?family=Old+Standard+TT:wght@400;700&display=swap">
<style>
  :root {
    --page: #eee6da;
    --label-black: #1c1c1c;
    --gold: #c98f1c;
    --gold-light: #e4b552;
    --ink: #161616;
    --type-gold: #c9952e;
  }
  html, body {
    margin: 0;
    padding: 0;
    width: 1200px;
    height: 1200px;
    overflow: hidden;
    background: var(--page);
  }
  .canvas {
    position: relative;
    width: 1200px;
    height: 1200px;
  }
  .label {
    position: absolute;
    left: 250px;
    top: 144px;
    width: 700px;
    height: 912px;
    background: var(--label-black);
    font-family: "Old Standard TT", "Times New Roman", serif;
  }
  .label__disc {
    position: absolute;
    left: 12px;
    top: 60px;
    width: 676px;
    height: 676px;
    border-radius: 50%;
    background: var(--gold);
  }
  .label__name {
    position: absolute;
    left: 0;
    top: 135px;
    width: 570px;
    text-align: right;
    color: var(--ink);
    margin: 0;
    font-weight: 400;
  }
  .label__name-main {
    display: block;
    font-size: 100px;
    line-height: 1;
    letter-spacing: -1px;
  }
  .label__name-sub {
    display: block;
    font-size: 46px;
    line-height: 1;
    margin-top: 0;
  }
  .label__mark {
    position: absolute;
    left: 130px;
    top: 400px;
    width: 440px;
    display: flex;
    align-items: center;
    justify-content: center;
    gap: 18px;
    color: var(--ink);
    font-size: 44px;
    font-weight: 400;
  }
  .label__mark-dot {
    width: 40px;
    height: 40px;
    border-radius: 50%;
    background: var(--ink);
    flex: none;
  }
  .label__variety {
    position: absolute;
    left: 0;
    top: 660px;
    width: 700px;
    text-align: center;
    color: var(--gold-light);
    font-size: 44px;
    line-height: 1;
    letter-spacing: 2px;
    margin: 0;
  }
  .label__origin {
    position: absolute;
    left: 0;
    top: 815px;
    width: 700px;
    text-align: center;
    color: var(--type-gold);
    font-size: 38px;
    line-height: 1;
    margin: 0;
  }
</style>
</head>
<body>
  <div class="canvas">
    <section class="label">
      <div class="label__disc"></div>
      <h1 class="label__name">
        <span class="label__name-main">Viento</span>
        <span class="label__name-sub">Callado</span>
      </h1>
      <div class="label__mark">
        <span class="label__mark-dot"></span>
        <span class="label__mark-text">Viento Callado</span>
      </div>
      <p class="label__variety">MALBEC</p>
      <p class="label__origin">Mendoza, Argentina</p>
    </section>
  </div>
</body>
</html>
```